Custom Business Card Design

We are looking for a raised spot logo design to use with Tavu.com. We will provide the logo files. Should be a front and back design. We want to implement the house into the back design using the same colors as the logo through out. Something VERY cool!

```html
<!DOCTYPE html>
<html lang="en">
<head>
<meta charset="utf-8">
<title>Tavu Business Card</title>
<link href="https://fonts.googleapis.com/css2?family=Montserrat:wght@400;500;600;700&display=swap" rel="stylesheet">
<style>
  :root {
    --brand-blue: #2f73b8;
    --brand-blue-light: #3a80c4;
    --brand-blue-deep: #2866a7;
    --brand-red: #e8474d;
    --ink: #3a3a3a;
    --paper: #ffffff;
    --stage: #e9ebee;
  }
  * { margin: 0; padding: 0; box-sizing: border-box; }
  html, body { width: 1200px; height: 900px; overflow: hidden; }
  body {
    background: var(--stage);
    font-family: "Montserrat", sans-serif;
    position: relative;
  }
  .card {
    position: absolute;
    width: 640px;
    height: 366px;
    left: 280px;
    border-radius: 4px;
    overflow: hidden;
    box-shadow: 0 8px 24px rgba(0,0,0,0.18);
  }
  .card-front { top: 48px; background: var(--paper); }
  .card-back { top: 486px; }

  .waves { position: absolute; inset: 0; width: 100%; height: 100%; }

  .brand {
    position: absolute;
    left: 44px;
    top: 56px;
    display: flex;
    align-items: center;
    gap: 12px;
  }
  .brand-mark {
    width: 22px; height: 22px;
    background: var(--brand-blue);
  }
  .brand-name {
    font-size: 44px;
    font-weight: 700;
    color: var(--brand-blue);
    letter-spacing: 0.5px;
  }

  .divider {
    position: absolute;
    left: 60px; right: 50px;
    top: 180px;
    height: 1.5px;
    background: var(--brand-blue);
  }
  .side-tab {
    position: absolute;
    right: 0; top: 166px;
    width: 10px; height: 40px;
    background: var(--brand-blue);
    border-radius: 6px 0 0 6px;
  }

  .person {
    position: absolute;
    right: 52px;
    top: 138px;
    text-align: right;
  }
  .person-name {
    font-size: 22px;
    font-weight: 500;
    color: var(--brand-blue);
    letter-spacing: 0.5px;
  }
  .person-name .surname { color: var(--brand-red); }
  .person-role {
    position: absolute;
    right: 52px;
    top: 188px;
    font-size: 16px;
    color: var(--ink);
  }

  .contact {
    position: absolute;
    left: 60px;
    top: 192px;
    list-style: none;
    font-size: 15px;
    color: var(--ink);
    letter-spacing: 0.6px;
  }
  .contact li { display: flex; align-items: center; gap: 12px; height: 22px; }
  .contact svg { width: 13px; height: 13px; flex: none; }

  .address {
    position: absolute;
    right: 52px;
    top: 226px;
    text-align: right;
    font-size: 15px;
    line-height: 22px;
    color: var(--ink);
    letter-spacing: 0.6px;
  }

  .star-field {
    position: absolute;
    inset: 0;
    background: linear-gradient(135deg, var(--brand-blue-light) 0%, var(--brand-blue) 50%, var(--brand-blue-deep) 100%);
  }
</style>
</head>
<body>

<section class="card card-front">
  <svg class="waves" viewBox="0 0 640 366" preserveAspectRatio="none" aria-hidden="true">
    <path d="M0,300 C80,330 160,348 250,356 C160,362 70,352 0,334 Z" fill="var(--brand-red)"/>
    <path d="M0,262 C100,310 220,336 380,343 C220,348 100,326 0,284 Z" fill="var(--brand-blue)"/>
    <path d="M250,348 C400,328 540,302 640,282 L640,312 C540,320 420,332 250,348 Z" fill="var(--brand-red)"/>
    <path d="M0,366 C150,368 300,352 420,338 C520,327 590,321 640,318 L640,366 Z" fill="var(--brand-blue)"/>
  </svg>

  <div class="brand">
    <span class="brand-mark"></span>
    <span class="brand-name">Tavu</span>
  </div>

  <div class="divider"></div>
  <div class="side-tab"></div>

  <div class="person">
    <div class="person-name">DANA <span class="surname">MORROW</span></div>
  </div>
  <div class="person-role">Founder</div>

  <ul class="contact">
    <li>
      <svg viewBox="0 0 12 12"><rect x="3" y="0.5" width="6" height="11" rx="1" fill="none" stroke="var(--brand-blue)" stroke-width="1.2"/></svg>
      0400 555 019
    </li>
    <li>
      <svg viewBox="0 0 12 12"><rect x="0.5" y="2" width="11" height="8" fill="var(--brand-blue)"/><path d="M0.5,2 L6,6.5 L11.5,2" fill="none" stroke="#fff" stroke-width="1"/></svg>
      info@tavu.com
    </li>
    <li>
      <svg viewBox="0 0 12 12"><circle cx="5" cy="5" r="3.6" fill="none" stroke="var(--brand-blue)" stroke-width="1.8"/><line x1="7.6" y1="7.6" x2="11" y2="11" stroke="var(--brand-blue)" stroke-width="1.8"/></svg>
      www.tavu.com
    </li>
  </ul>

  <div class="address">
    1820 Harbor Ave<br>
    mailing New York, USA
  </div>
</section>

<section class="card card-back">
  <div class="star-field" role="img" aria-label="Embossed tone-on-tone star pattern covering the card back"></div>
</section>

</body>
</html>
```